Business Card Design

building company specialistloft conversion,extension ,bathrooms ,kitchens ,painting and decorating all general building work

Industry/Entity Type

Building

Contact Information for Business Card

K&R Home renewal Ltd
tel -07912468305
email-Rmarek07@brickmail.example
web in progres

Font styles to use
Sans Serif

Requirements
Must have
• name of the company
• all contact details
Nice to have
• some of the skills

```html
<!DOCTYPE html>
<html lang="en">
<head>
<meta charset="utf-8">
<title>K&amp;R Home renewal Ltd – Business Card</title>
<link rel="stylesheet" href="https://fonts.googleapis.com/css2?family=Lato:wght@400;700&family=Cinzel:wght@400&display=swap">
<style>
  :root {
    --canvas: #ecebf1;
    --purple-light: #8f90d4;
    --purple: #5350b0;
    --purple-deep: #2a2377;
    --brand: #3f3a9c;
    --ink: #3b3b4a;
    --grey-stripe: #8b8b93;
    --white: #ffffff;
  }
  * { margin: 0; padding: 0; box-sizing: border-box; }
  html, body { width: 1200px; height: 913px; overflow: hidden; }
  body {
    background: var(--canvas);
    font-family: "Lato", Arial, sans-serif;
    position: relative;
  }
  .card {
    position: absolute;
    width: 560px;
    height: 320px;
    border-radius: 3px;
    overflow: hidden;
    box-shadow: 0 6px 18px rgba(40, 35, 90, .18);
  }

  /* ---------- Back of card ---------- */
  .card-back {
    left: 60px; top: 80px;
    background: linear-gradient(170deg, var(--purple-light) 0%, var(--purple) 55%, var(--purple-deep) 100%);
    color: var(--white);
  }
  .card-back .brand {
    position: absolute; left: 40px; top: 150px; width: 230px; text-align: center;
  }
  .brand-name {
    font-family: "Lato", Arial, sans-serif;
    font-weight: 400;
    letter-spacing: .04em;
    text-transform: uppercase;
    line-height: 1.15;
  }
  .card-back .brand-name { font-size: 24px; color: var(--white); }
  .brand-rule { display: block; height: 1px; margin: 8px auto 0; width: 88%; }
  .card-back .brand-rule { background: var(--white); }
  .card-back .divider {
    position: absolute; left: 290px; top: 120px; width: 1px; height: 90px; background: rgba(255,255,255,.8);
  }
  .services { position: absolute; left: 315px; top: 118px; font-size: 14px; line-height: 1.5; }
  .services h2 { font-size: 14px; font-weight: 700; }
  .services ul { list-style: none; }
  .services li::before { content: "• "; }
  .card-back .web {
    position: absolute; right: 36px; bottom: 34px; font-size: 13px; letter-spacing: .18em;
  }

  /* ---------- Front of card ---------- */
  .card-front { left: 580px; top: 510px; background: var(--white); color: var(--ink); }
  .card-front .brand { position: absolute; left: 34px; top: 40px; width: 240px; text-align: center; }
  .card-front .brand-name { font-size: 22px; color: var(--brand); }
  .card-front .brand-rule { background: var(--brand); }
  .person { position: absolute; right: 40px; top: 46px; text-align: right; }
  .person-name { font-family: "Cinzel", Georgia, serif; font-size: 19px; color: var(--brand); }
  .person-role { font-size: 13px; color: var(--ink); }
  .address { position: absolute; left: 40px; top: 132px; font-size: 13px; line-height: 1.35; }
  .address strong { color: var(--brand); }
  .contacts { position: absolute; left: 40px; top: 200px; list-style: none; font-size: 13px; line-height: 1.45; }
  .contacts li { display: flex; align-items: center; gap: 10px; }
  .contacts svg { width: 13px; height: 13px; fill: var(--brand); flex: none; }
  .swoosh { position: absolute; left: 0; top: 0; }
  .card-front .web {
    position: absolute; right: 24px; bottom: 112px; font-size: 12px; color: var(--white);
    transform: rotate(-14deg); transform-origin: right bottom;
  }
</style>
</head>
<body>

<section class="card card-back" aria-label="Business card back">
  <div class="brand">
    <div class="brand-name">K&amp;R Home renewal Ltd</div>
    <span class="brand-rule"></span>
  </div>
  <span class="divider"></span>
  <div class="services">
    <h2>Our Services:</h2>
    <ul>
      <li>Extension • Bathrooms</li>
      <li>Kitchens • Painting</li>
      <li>Decorating all general building work</li>
    </ul>
  </div>
  <div class="web">WWW.WEBSITE.COM</div>
</section>

<section class="card card-front" aria-label="Business card front">
  <svg class="swoosh" width="560" height="320" viewBox="0 0 560 320" aria-hidden="true">
    <path d="M130,320 C250,300 330,210 560,150 L560,320 Z" fill="var(--purple)"/>
    <path d="M150,320 C270,292 345,196 560,132" fill="none" stroke="var(--grey-stripe)" stroke-width="4"/>
  </svg>
  <div class="brand">
    <div class="brand-name">K&amp;R Home renewal Ltd</div>
    <span class="brand-rule"></span>
  </div>
  <div class="person">
    <div class="person-name">Daniel Carver</div>
    <div class="person-role">Managing Director</div>
  </div>
  <address class="address" style="font-style:normal">
    <strong>K&amp;R Home renewal Ltd</strong><br>
    Suite 123 Street Name<br>
    State, Zip 1234, Country Name
  </address>
  <ul class="contacts">
    <li><svg viewBox="0 0 16 16"><path d="M3 1h3l1.5 4-2 1.2a9 9 0 0 0 4.3 4.3L11 8.5l4 1.5v3c0 1-1 2-2 2C6.5 15 1 9.5 1 3c0-1 1-2 2-2z"/></svg>079.1246.8305</li>
    <li><svg viewBox="0 0 16 16"><path d="M4 0h8a1 1 0 0 1 1 1v14a1 1 0 0 1-1 1H4a1 1 0 0 1-1-1V1a1 1 0 0 1 1-1zm0 2v11h8V2z"/></svg>000.0000.0000</li>
    <li><svg viewBox="0 0 16 16"><path d="M4 1h8v4H4zM1 6h14v7h-3v2H4v-2H1zm4 5v3h6v-3z"/></svg>000.0000.0000</li>
    <li><svg viewBox="0 0 16 16"><path d="M0 3h16v10H0zm1.5 1.5L8 9l6.5-4.5z" fill-rule="evenodd"/></svg>Rmarek07@brickmail.example</li>
  </ul>
  <div class="web">www.website.com</div>
</section>

</body>
</html>
```